Web Design Project

I work in a sign company that print banners, back light films, and vinyl lettering. We also create metal store signs that lights up. We have a laser cutter that can cut plastics and a waterjet that can cut stainless steel.
Job: Create a homepage
Requirements:
1. Keep it simple and neat, I do not want it to be messy. (Similar to this website, plover, or this http://www.markelvo.example/)
2. A navigation bar that has (Will help if you show a template for one of these links):
-Home
-Signs
-Banners
-Lettering
-Prints
-Gallery
3.Bottom of the page
-Abous us
-Shipping and Returning Policy
-Resellers
4.Other (Somewhere easy to find)
-Login
-Shopping Cart
-Upload
Updates
Nice job designers. I am currently working on the Site's logo, so I will be posting that up later.
I would like you guys to change the selection on the navigation bar.
It should only have:
Banners
Lettering
Prints
Gallery
Keep up the good work
Sorry for the bad update, the Navigation bar should have:
Home
Signs
Banners
Lettering
Prints
Gallery

```html
<!DOCTYPE html>
<html lang="en">
<head>
<meta charset="utf-8">
<title>Company Name – Signs, Banners &amp; Lettering</title>
<link href="https://fonts.googleapis.com/css2?family=Noto+Sans:ital,wght@0,400;0,500;0,700;1,400;1,500&display=swap" rel="stylesheet">
<style>
:root{
  --green:#8cc21f;
  --green-dark:#6fa10e;
  --green-light:#c3e04a;
  --ink:#222;
  --text:#666;
  --muted:#888;
  --blue:#1e9be0;
  --navy:#0f1d2c;
  --panel:#ededed;
  --line:#d6d6d6;
}
*{box-sizing:border-box;margin:0;padding:0}
html,body{width:1175px;height:1200px;overflow:hidden}
body{position:relative;background:#fff;font-family:"Noto Sans",sans-serif;color:var(--text)}
a{text-decoration:none;color:inherit}
.abs{position:absolute}

.site-header{position:absolute;left:0;top:0;width:1175px;height:128px;background:linear-gradient(#f9f9f9,#ececec)}
.utility-links{position:absolute;right:165px;top:7px;font-size:11px;color:#555;display:flex;gap:8px}
.utility-links .sep{color:#999}
.cart-icon{display:inline-block;vertical-align:-2px;margin-right:3px}
.brand{position:absolute;left:167px;top:36px;font-size:27px;font-weight:700;color:var(--green);letter-spacing:-1px}
.hotline{position:absolute;left:686px;top:46px;font-size:22px;color:#8a8a8a;letter-spacing:.5px}
.hotline .number{position:absolute;left:161px;top:-5px;white-space:nowrap;font-size:27px;font-style:italic;color:var(--blue);letter-spacing:1px}

.main-nav{position:absolute;left:0;top:95px;width:1175px;height:33px;background:linear-gradient(#fafafa,#e9e9e9);border-bottom:1px solid #dcdcdc}
.main-nav a{position:absolute;top:7px;font-size:13.5px;color:var(--ink)}
.main-nav .home-tab{position:absolute;left:167px;top:0;width:98px;height:33px}
.main-nav .home-tab span{position:absolute;left:31px;top:7px;color:#fff;font-size:13.5px}

.dark-strip{position:absolute;left:0;top:128px;width:1175px;height:13px;background:var(--navy)}
.green-band{position:absolute;left:0;top:141px;width:1175px;height:472px;background:linear-gradient(var(--green-light),var(--green) 60%,#86bb1a)}
.hero{position:absolute;left:167px;top:128px;width:843px;height:485px;background:radial-gradient(circle at 60% 45%,#f6f6f6,#e6e6e6)}
.hero-art{position:absolute;left:0;top:0;width:379px;height:433px;background:linear-gradient(#1f7fd6 0 12%,#f4ec10 12% 28%,#e0190f 28% 42%,#f39a80 42% 55%,#d8c1a3 55% 63%,#f57a22 63% 80%,#f4ec10 80%)}
.hero-confetti{position:absolute;left:379px;top:0;width:464px;height:55px;background:linear-gradient(90deg,#3fa32a,#f4ec10 40%,#1e9be0 75%,#f4d010)}
.testimonial{position:absolute;left:390px;top:143px;width:420px;text-align:center}
.testimonial h2{font-size:26px;font-weight:400;font-style:italic;color:var(--green)}
.testimonial p{margin-top:10px;font-size:16.3px;line-height:26.4px;font-style:italic;color:#555}
.service-tabs{position:absolute;left:245px;top:561px;display:flex;gap:3px}
.service-tabs a{width:229px;height:52px;border:1px solid #ccc;border-bottom:0;border-radius:4px 4px 0 0;background:linear-gradient(#fafafa,#ececec);color:#8b8b8b;font-size:21px;text-align:center;line-height:52px}
.service-tabs a.active{background:var(--green);border-color:var(--green);color:#fff}

.column{position:absolute;top:645px;width:263px}
.column h3{font-size:16.5px;font-weight:500;color:var(--green);padding-bottom:4px;border-bottom:1px solid var(--line);height:25px}
.column .body{font-size:12.8px;line-height:19.4px;color:#777}
.col-welcome{left:167px}
.col-welcome .body{margin-top:20px;padding-left:2px}
.col-welcome .body p+p{margin-top:13px}
.col-featured{left:454px}
.project-thumb{position:absolute;left:40px;top:48px;width:190px;height:78px;background:linear-gradient(90deg,#5a4a6a,#2f2a30 30%,#d9d2c8 45%,#6b5a4b 60%,#d47a20 85%,#f2f2f2)}
.project-name{position:absolute;left:0;top:140px;font-size:13.5px;color:#333}
.col-featured .body{position:absolute;top:163px;left:0;width:263px}
.col-start{left:746px}
.signup{position:absolute;left:0;top:40px;width:264px;height:124px;border:1px solid #d2d2d2;border-radius:3px;background:linear-gradient(#fff,#f0f0f0)}
.signup .title{position:absolute;left:77px;top:20px;font-size:16.5px;color:#555}
.signup .mail{position:absolute;left:34px;top:11px}
.signup .email{position:absolute;left:41px;top:55px;width:182px;height:24px;border:1px solid #ddd;border-radius:3px;background:#fff;font-size:12px;font-style:italic;color:#bbb;text-align:center;line-height:22px}
.signup .cta{position:absolute;left:74px;top:87px;width:114px;height:26px;border-radius:13px;background:linear-gradient(#a6d63a,#6ea611);color:#fff;font-size:13px;font-weight:700;text-align:center;line-height:26px}
.quick-links{position:absolute;left:4px;top:186px;list-style:none}
.quick-links li{font-size:13.3px;color:#333;height:26.4px;padding-left:14px;position:relative}
.quick-links li::before{content:"";position:absolute;left:0;top:7px;width:5px;height:5px;border-radius:50%;background:var(--green)}

.more-link{position:absolute;top:1014px;width:263px;border-top:1px solid var(--line);padding-top:12px;padding-left:2px;font-size:13.5px;color:var(--green);text-decoration:underline}

.footer-rule{position:absolute;left:165px;top:1076px;width:845px;height:4px;background:#e2e2e2;box-shadow:0 2px 4px rgba(0,0,0,.08)}
.footer-links{position:absolute;left:0;top:1114px;width:1175px;text-align:center;font-size:11px;color:var(--muted)}
.footer-links .sep{margin:0 9px}
.footer-links .social{color:#3b5b99;font-weight:500}
.copyright{position:absolute;left:0;top:1148px;width:1175px;text-align:center;font-size:11px;color:var(--muted)}
</style>
</head>
<body>

<header class="site-header">
  <nav class="utility-links">
    <a href="#">My Account</a><span class="sep">|</span>
    <a href="#">Log In</a><span class="sep">|</span>
    <a href="#"><svg class="cart-icon" width="13" height="11" viewBox="0 0 13 11"><path d="M0 1h2.5l1.8 6h6.5l1.7-4.5H4" fill="none" stroke="#1e7bc0" stroke-width="1.4"/><circle cx="5" cy="9.5" r="1.2" fill="#1e7bc0"/><circle cx="10" cy="9.5" r="1.2" fill="#1e7bc0"/></svg>My Cart (0)<span style="color:var(--blue)"> ▾</span></a><span class="sep">|</span>
    <a href="#">Checkout</a>
  </nav>
  <div class="brand">LOGO</div>
  <div class="hotline">HOT ONLINE:<span class="number">111-111-1111</span></div>
</header>

<nav class="main-nav">
  <a class="home-tab" href="#"><svg width="98" height="33" viewBox="0 0 98 33" style="position:absolute;left:0;top:0"><polygon points="16,0 98,0 82,33 0,33" fill="#8cc21f"/></svg><span>Home</span></a>
  <a href="#" style="left:287px">About Us</a>
  <a href="#" style="left:401px">Signs</a>
  <a href="#" style="left:493px">Banners</a>
  <a href="#" style="left:597px">Lettering</a>
  <a href="#" style="left:711px">Prints</a>
  <a href="#" style="left:795px">Gallery</a>
  <a href="#" style="left:897px">Contact Us</a>
</nav>

<div class="dark-strip"></div>
<div class="green-band"></div>

<section class="hero">
  <div class="hero-art" role="img" aria-label="Illustration of colourful banner stripes with rolled printed banners"></div>
  <div class="hero-confetti" role="img" aria-label="Illustration of colourful ribbons and confetti"></div>
  <div class="testimonial">
    <h2>What our clients say</h2>
    <p>I just wanted to let your company know how pleased we are with the banner.&nbsp; The quality is wonderful, and the turn-around time was incred-ible.&nbsp; Thank you for such excellent work.</p>
  </div>
</section>

<nav class="service-tabs">
  <a class="active" href="#">PRINT BANNERS</a>
  <a href="#">BACK LIGHT FILMS</a>
  <a href="#">VINYI&nbsp; LETTERING</a>
</nav>

<section class="column col-welcome">
  <h3>Welcome to Company Name</h3>
  <div class="body">
    <p>I work in a sign company that print ban-ners, back light films, and vinyl lettering. We also create metal store signs that lights up.</p>
    <p>We are proud of our capacity to respond to client needs, and count many large and medium sized companies among our clients. We have a long history of deliver-ing complex projects on time, on budget and ensuring a high level of client satis-faction.</p>
    <p>...can deliver all or part of your corporate signage requirements. We can act as your full service supplier, or work with other firms to complete a project.</p>
  </div>
</section>

<section class="column col-featured">
  <h3>Featured Projects</h3>
  <div class="project-thumb" role="img" aria-label="Photo of three printed roll-up banner stands"></div>
  <div class="project-name">Project name</div>
  <div class="body">Main content description of this relevant project, Main content description of this relevant project, Main content description of this relevant project, Main content de-scription of this relevant project, Main content description of this relevant proj-ect, Main content description of this rel-evant project, Main content description of this relevant project.</div>
</section>

<section class="column col-start">
  <h3>Start Here</h3>
  <div class="signup">
    <svg class="mail" width="36" height="34" viewBox="0 0 36 34"><rect x="2" y="12" width="32" height="20" rx="2" fill="#e8edf2" stroke="#9fb0c0"/><path d="M2 14l16 10 16-10" fill="none" stroke="#9fb0c0"/><rect x="9" y="2" width="18" height="14" fill="#4aa3dc"/><path d="M12 6h12M12 9h12M12 12h8" stroke="#fff"/></svg>
    <div class="title">GET AN ACCOUNT</div>
    <div class="email">john@mailbox.example</div>
    <a class="cta" href="#">Get it Now!</a>
  </div>
  <ul class="quick-links">
    <li>How to Order</li>
    <li>Why Buy xxx</li>
    <li>Quick Order Status</li>
    <li>How to get free sample kit</li>
    <li>Customer Support</li>
  </ul>
</section>

<a class="more-link" href="#" style="left:167px">Learn more about XXX &gt;&gt;</a>
<a class="more-link" href="#" style="left:454px">visit more about our galleries &gt;&gt;</a>
<a class="more-link" href="#" style="left:746px">Details of start here &gt;&gt;</a>

<div class="footer-rule"></div>
<footer>
  <div class="footer-links">
    <a href="#">Abous us</a><span class="sep">|</span>
    <a href="#">Shipping and Returning Policy</a><span class="sep">|</span>
    <a href="#">Resellers</a><span class="sep">|</span>
    <a class="social" href="#">Chatter</a><span class="sep">|</span>
    <a class="social" href="#">Workline</a><span class="sep">|</span>
    <a class="social" href="#">Vidcast</a>
  </div>
  <div class="copyright">Copyright © 2012-2017&nbsp; COMPANY NAME&nbsp; rights reserved.</div>
</footer>

</body>
</html>
```